Modern Yoga Studio Timetable and Flyer Design

We have a comprehensive class timetable and we are wanting to a clean modern look for our Spring timetable.

We require a double sided flyer with our class timetable included.
We would prefer an A5 size (postcard) or DL (1/3 A4).

We would like the final flyer to have.
Side A : Yoga image, logo

Fennel Stretch Hall
address: 4/71 Wexcombe Lane, Pelharton
website: fennelstretch.com.au
mobile: 0471 296 814

Side B: Clear easy to read timetable with a break down of class types and website.

We would also like to have a copy of the timetable itself as a separate jpg or pdf for use on our website to download.

Thank you.
Yours kindly,
Nell

I have attached a sample of another timetable of which I like the look and feel of, however this is just a guide. I've also attached our 'new' schedule in WORD plus uploaded our last design of the front.
Updates

Target Market(s)

Women aged 30-45

Industry/Entity Type

Health And Wellness

Font styles to use
Other font styles liked:
• Brandon Grotesque, Jenna Sue

Colors
6c459b
33a6d7
ffffff

Requirements
Must have
• A definitive colour to decipher between different class types on our timetable. Where each colour represents a different class type. Colours and layouts similar to our website design, see www.fennelstretch.com.au
Nice to have
• I've included a design of another studio whose timetable design I like. One of our own yoga images instead of a stock image.
Should not have
• No dark gridlines between the cells/boxes in the timetables. Please don't use stock yoga images.

```html
<!DOCTYPE html>
<html lang="en">
<head>
<meta charset="utf-8">
<title>Fennel Stretch Hall – Spring Flyer</title>
<link href="https://fonts.googleapis.com/css2?family=Montserrat:wght@300;400;500;600;700&family=Caveat:wght@500&display=swap" rel="stylesheet">
<style>
  :root{
    --purple:#6c459b;
    --purple-deep:#4a2a7e;
    --blue:#33a6d7;
    --blue-soft:#d9eef9;
    --row-blue:#dff0fb;
    --row-grey:#e3e3e9;
    --ink:#333338;
    --header:#3a3a3f;
    --cls-vinyasa:#6c459b;
    --cls-slow:#33a6d7;
    --cls-family:#58585c;
    --cls-youth:#23204f;
    --cls-gentle:#ffffff;
    --white:#ffffff;
    --stage:#efedf2;
  }
  *{box-sizing:border-box;margin:0;padding:0}
  html,body{width:902px;height:1200px;overflow:hidden;background:var(--stage);font-family:"Montserrat",sans-serif}
  .canvas{position:relative;width:902px;height:1200px}

  /* Side A */
  .flyer-front{position:absolute;left:225px;top:37px;width:448px;height:626px;background:var(--white);box-shadow:0 6px 18px rgba(0,0,0,.18);overflow:hidden}
  .flyer-front > svg{position:absolute;inset:0}
  .front-logo{position:absolute;top:88px;left:0;width:100%;text-align:center;color:var(--blue);font-weight:300;font-size:22px;letter-spacing:5px}
  .front-name{position:absolute;top:518px;left:0;width:100%;text-align:center;color:var(--white);font-family:"Caveat",cursive;font-size:34px;line-height:40px}
  .contact-bar{position:absolute;left:22px;top:568px;width:404px;height:28px;display:flex;align-items:center;justify-content:space-between;padding:0 8px;color:var(--white);font-size:8px;font-weight:500;white-space:nowrap}
  .contact-item{display:flex;align-items:center;gap:5px}
  .contact-item svg{width:10px;height:10px;flex:none}

  /* Side B */
  .flyer-back{position:absolute;left:135px;top:690px;width:627px;height:448px;background:var(--white);box-shadow:0 6px 18px rgba(0,0,0,.18);overflow:hidden}
  .back-band-top{position:absolute;top:0;left:0;width:100%;height:20px;background:var(--blue);border-bottom:2px solid var(--purple)}
  .back-logo{position:absolute;top:50px;left:20px;color:var(--blue);font-weight:300;font-size:11px;letter-spacing:2px;white-space:nowrap}
  .back-title{position:absolute;top:46px;right:20px;font-size:18px;font-weight:700;color:var(--blue);letter-spacing:.2px;white-space:nowrap}
  .back-title span{color:var(--purple)}
  .timetable{position:absolute;left:17px;top:96px;width:593px;border-collapse:separate;border-spacing:2px;background:var(--white);box-shadow:0 0 0 2px var(--purple),0 3px 8px rgba(0,0,0,.25)}
  .timetable th{background:var(--header);color:var(--white);font-size:10px;font-weight:600;height:27px}
  .timetable td{height:19.5px;font-size:6.5px;font-weight:600;text-align:center;padding:0 2px;white-space:nowrap}
  .timetable td.time{text-align:left;padding-left:7px;color:var(--ink)}
  .timetable tr:nth-child(odd) td{background:var(--row-blue)}
  .timetable tr:nth-child(even) td{background:var(--row-grey)}
  .timetable tr td.vinyasa{background:var(--cls-vinyasa);color:var(--white)}
  .timetable tr td.slow{background:var(--cls-slow);color:var(--white)}
  .timetable tr td.family{background:var(--cls-family);color:var(--white)}
  .timetable tr td.youth{background:var(--cls-youth);color:var(--white)}
  .timetable tr td.gentle{background:var(--cls-gentle);color:var(--ink)}
  .back-band-bottom{position:absolute;bottom:0;left:0;width:100%;height:33px;background:var(--blue);border-top:2px solid var(--purple);color:var(--white);font-size:10px;letter-spacing:3px;text-align:center;line-height:31px}
</style>
</head>
<body>
<div class="canvas">

  <section class="flyer-front">
    <svg viewBox="0 0 448 626" width="448" height="626">
      <defs>
        <linearGradient id="ringBlue" x1="0" y1="0" x2="0" y2="1">
          <stop offset="0" stop-color="#5cbbe3"/><stop offset="1" stop-color="#2a93c7"/>
        </linearGradient>
        <linearGradient id="photoTone" x1="0" y1="0" x2="0" y2="1">
          <stop offset="0" stop-color="#f4f3f1"/><stop offset=".55" stop-color="#d9c9c4"/><stop offset=".8" stop-color="#b89a72"/><stop offset="1" stop-color="#a98a62"/>
        </linearGradient>
        <linearGradient id="basePurple" x1="0" y1="0" x2="0" y2="1">
          <stop offset="0" stop-color="#7a52aa"/><stop offset="1" stop-color="#4a2a7e"/>
        </linearGradient>
        <linearGradient id="barBlue" x1="0" y1="0" x2="1" y2="0">
          <stop offset="0" stop-color="#5a3a8e"/><stop offset=".5" stop-color="#33a6d7"/><stop offset="1" stop-color="#5a3a8e"/>
        </linearGradient>
        <clipPath id="photoClip"><circle cx="224" cy="340" r="188"/></clipPath>
      </defs>
      <rect width="448" height="20" fill="#33a6d7"/>
      <rect y="20" width="448" height="2" fill="#6c459b"/>
      <path d="M0 250 Q40 215 70 190 Q30 300 70 420 Q30 440 0 450Z" fill="#d9eef9"/>
      <path d="M448 250 Q408 215 378 190 Q418 300 378 420 Q418 440 448 450Z" fill="#d9eef9"/>
      <circle cx="224" cy="355" r="207" fill="url(#ringBlue)"/>
      <circle cx="224" cy="345" r="200" fill="#6c459b"/>
      <circle cx="224" cy="340" r="192" fill="#ffffff"/>
      <g role="img" aria-label="Photo of a yoga teacher holding a twisted side-angle pose on a jute mat" clip-path="url(#photoClip)">
        <rect x="30" y="150" width="390" height="380" fill="url(#photoTone)"/>
      </g>
      <path d="M0 470 Q224 505 448 470 L448 626 L0 626Z" fill="#33a6d7"/>
      <path d="M0 480 Q224 520 448 480 L448 626 L0 626Z" fill="#ffffff"/>
      <path d="M0 484 Q224 524 448 484 L448 626 L0 626Z" fill="url(#basePurple)"/>
      <rect x="22" y="568" width="404" height="28" fill="url(#barBlue)"/>
      <rect y="606" width="448" height="3" fill="#ffffff"/>
      <rect y="609" width="448" height="17" fill="#33a6d7"/>
    </svg>

    <div class="front-logo">fennel stretch hall</div>
    <div class="front-name">Fennel Stretch Hall</div>

    <div class="contact-bar">
      <span class="contact-item">
        <svg viewBox="0 0 12 12"><path d="M3 1l2 2.5-1.2 1.2a6 6 0 0 0 3.5 3.5L8.5 7 11 9l-1.5 2C5 11 1 7 1 2.5Z" fill="none" stroke="#fff" stroke-width="1"/></svg>
        0471 296 814
      </span>
      <span class="contact-item">
        <svg viewBox="0 0 12 12"><circle cx="6" cy="6" r="5" fill="none" stroke="#fff"/><path d="M1 6h10M6 1c-3 3-3 7 0 10M6 1c3 3 3 7 0 10" fill="none" stroke="#fff" stroke-width=".8"/></svg>
        www.fennelstretch.com.au
      </span>
      <span class="contact-item">
        <svg viewBox="0 0 12 12"><path d="M6 11S2 6.8 2 4.5a4 4 0 0 1 8 0C10 6.8 6 11 6 11Z" fill="none" stroke="#fff"/><circle cx="6" cy="4.5" r="1.4" fill="#fff"/></svg>
        4/71 Wexcombe Lane, Pelharton
      </span>
    </div>
  </section>

  <section class="flyer-back">
    <div class="back-band-top"></div>
    <div class="back-logo">fennel stretch hall</div>
    <h1 class="back-title">FENNEL STRETCH SPRING <span>TIMETABLE</span></h1>

    <table class="timetable">
      <colgroup>
        <col style="width:58px"><col style="width:76px"><col style="width:79px"><col style="width:74px"><col style="width:83px"><col style="width:71px"><col style="width:73px"><col style="width:61px">
      </colgroup>
      <thead>
        <tr><th>TIME</th><th>MON</th><th>TUE</th><th>WED</th><th>THU</th><th>FRI</th><th>SAT</th><th>SUN</th></tr>
      </thead>
      <tbody>
        <tr><td class="time">5:45AM</td><td></td><td class="gentle">RISE + SHINE*</td><td></td><td class="gentle">RISE + SHINE*</td><td></td><td></td><td></td></tr>
        <tr><td class="time">9:00AM</td><td></td><td></td><td></td><td></td><td></td><td class="vinyasa">VINYASA FLOW</td><td></td></tr>
        <tr><td class="time">9:15AM</td><td></td><td class="vinyasa">VINYASA FLOW</td><td></td><td></td><td></td><td></td><td class="gentle">YIN</td></tr>
        <tr><td class="time">9:30AM</td><td class="slow">SLOW FLOW</td><td></td><td></td><td class="vinyasa">VINYASA FLOW</td><td></td><td></td><td></td></tr>
        <tr><td class="time">10:30AM</td><td></td><td></td><td></td><td></td><td></td><td class="family">PREGNANCY*</td><td></td></tr>
        <tr><td class="time">11AM</td><td></td><td class="family">MUM + BABY*</td><td></td><td class="family">MUM + BABY*</td><td></td><td></td><td></td></tr>
        <tr><td class="time">12:15PM</td><td></td><td></td><td class="youth">KIDS (8-12*)</td><td class="family">PREGNANCY</td><td></td><td></td><td></td></tr>
        <tr><td class="time">4PM</td><td></td><td></td><td class="youth">TEENS (12-16*)</td><td class="youth">KIDS (5- 7*)</td><td></td><td class="vinyasa">VINYASA FLOW</td><td></td></tr>
        <tr><td class="time">4:45PM</td><td></td><td></td><td></td><td></td><td></td><td></td><td></td></tr>
        <tr><td class="time">5:00PM</td><td></td><td></td><td></td><td class="youth">TEENS (12 – 16*)</td><td></td><td></td><td></td></tr>
        <tr><td class="time">6:00PM</td><td class="family">PREGNANCY*</td><td class="vinyasa">VINYASA FLOW</td><td class="slow">SLOW FLOW</td><td></td><td class="gentle">FLOW + RESTORE</td><td></td><td></td></tr>
        <tr><td class="time">6:15PM</td><td></td><td></td><td></td><td class="family">PREGNANCY*</td><td></td><td></td><td></td></tr>
        <tr><td class="time">7:30PM</td><td class="vinyasa">VINYASA FLOW</td><td class="family">PREGNANCY*</td><td class="gentle">YIN + RESTORE</td><td class="gentle">WOMEN'S WELLNESS*</td><td></td><td></td><td></td></tr>
      </tbody>
    </table>

    <div class="back-band-bottom">www.fennelstretch.com.au</div>
  </section>

</div>
</body>
</html>
```